CoverLantern.com website re-design - modern engaging website creation

We have an existing website. Www.CoverLantern.com - the content on the site and our widgets are custom built. But the layout and design of our site we just put there as we built the functionality around it. We want a new, bold, and modern design aimed at getting visitors to run a life insurance quote and ultimately apply. Our demographic is centered around those between the ages of 30-60. So we are looking at a complete site overhaul with better pictures, buttons, and an extremely modern design.

Target Market(s)

30-50 year olds

Industry/Entity Type

Life insurance

Coding

Coded - Design and coding required

Number of Pages Required

5+ page

Font styles to use
Other font styles liked:
• Rubik

Colors
0054AA
0677BA
7BADD7
CADEEF
E8F1F8
00AB8E
00BBA5
67D7C9
C6EFE9
E9F9F6
59FF00
82FF00
B8FF75
E3FFCB
F4FFEA

Requirements
Must have
• Matching color schemes from existing website. We have custom widgets on our site now and those must be . White space is important to make it simple for the user to navigate
Nice to have
• Same content - different more modern design
Should not have
• Colors outside of our current color scheme. Should NOT be too similar to our existing site.

```html
<!DOCTYPE html>
<html lang="en">
<head>
<meta charset="utf-8">
<title>CoverLantern – Life insurance for a worryfree life</title>
<link href="https://fonts.googleapis.com/css2?family=Inter:wght@400;500;600;700&family=Roboto+Condensed:wght@400&display=swap" rel="stylesheet">
<style>
:root{
  --blue:#0068b1;
  --green:#8dc63f;
  --ink:#2b2f33;
  --text:#3a3f44;
  --muted:#7a8089;
  --panel:#f0f3f7;
  --dark:#30353b;
  --white:#ffffff;
}
*{box-sizing:border-box;margin:0;padding:0}
html,body{width:1200px;height:3069px;overflow:hidden;background:var(--white)}
body{position:relative;font-family:'Inter',sans-serif;color:var(--text)}
.abs{position:absolute}
a{color:inherit}
.brand{font-weight:500;color:var(--blue);font-size:36px;letter-spacing:-0.5px;white-space:nowrap}

/* nav */
.site-nav{left:650px;top:58px;display:flex;gap:20px;font-size:17px;font-weight:600;color:var(--ink)}
.site-nav .active{color:var(--blue)}

/* hero */
.hero-title{left:76px;top:212px;font-size:67px;font-weight:700;line-height:72px;color:var(--blue);letter-spacing:-1.5px;white-space:nowrap}
.hero-title .g{color:var(--green)}
.hero-lede{left:81px;top:386px;width:560px;font-size:19px;line-height:28px;color:var(--ink)}
.quote-label{left:81px;top:494px;font-size:19px;font-weight:600;color:var(--blue)}
.state-select{left:81px;top:539px;width:259px;height:46px;background:#e9ecef;border-radius:3px;font-size:19px;color:#8b9096;padding:12px 17px}
.state-select svg{position:absolute;right:16px;top:19px}
.btn{background:var(--green);color:var(--white);font-weight:600;border-radius:3px;display:flex;align-items:center;justify-content:center;white-space:nowrap}
.quote-btn{left:348px;top:539px;width:162px;height:46px;font-size:19px}
.hero-art{left:670px;top:140px;width:490px;height:470px}

/* how it works */
.how{left:0;top:697px;width:1200px;height:427px;background:var(--panel)}
.section-title{font-weight:700;color:var(--blue);letter-spacing:-0.5px}
.section-title .g{color:var(--green)}
.how-title{left:0;width:1200px;top:744px;text-align:center;font-size:43px}
.step{top:842px;width:350px}
.step-num{position:absolute;left:0;top:1px;width:26px;height:26px;border-radius:50%;background:var(--green);color:var(--white);font-size:16px;display:flex;align-items:center;justify-content:center}
.step h3{margin-left:43px;font-size:19px;font-weight:700;color:var(--blue);line-height:28px;white-space:nowrap}
.step p{margin-left:43px;margin-top:10px;font-size:18px;line-height:28px;color:var(--text)}
.step-link{top:1043px;font-size:19px;font-weight:600;color:var(--blue);text-decoration:underline}

/* compare */
.compare-title{left:75px;top:1182px;font-size:43px}
.bullets{left:75px;top:1272px;width:580px;list-style:none;font-size:18.5px;line-height:28px;color:var(--ink)}
.bullets li{position:relative;padding-left:29px;margin-bottom:13px}
.bullets li::before{content:"";position:absolute;left:0;top:12px;width:7px;height:7px;border-radius:50%;background:var(--green)}
.compare-btn{left:75px;top:1490px;width:200px;height:46px;font-size:19px}
.rate-card{left:760px;width:323px;height:117px;border:2px solid #e3e6ea;border-radius:5px;background:var(--white);display:flex;align-items:center}
.rate-card.best{border:3px solid var(--green)}
.rate-card .carrier{width:160px;text-align:center;font-size:27px;font-weight:500;color:var(--ink);border-right:1px solid #e3e6ea;height:80px;display:flex;align-items:center;justify-content:center}
.rate-card .terms{flex:1;text-align:center;font-family:'Roboto Condensed',sans-serif;font-size:13.5px;color:#555;line-height:21px}
.rate-card .price{font-family:'Inter',sans-serif;font-weight:700;color:var(--ink);font-size:34px;line-height:40px;margin-top:4px}
.rate-card .price small{font-size:18px;font-weight:500;vertical-align:14px}
.rate-card .price i{font-style:normal;font-size:13px;font-weight:500;display:inline-block;line-height:13px;text-align:left}

/* trusted */
.trusted{left:0;top:1639px;width:1200px;height:348px;background:var(--panel)}
.trusted-title{left:74px;top:1722px;font-size:42px;line-height:51px;width:700px}
.carrier-tile{background:var(--white);display:flex;align-items:center;justify-content:center;font-weight:700;color:var(--dark);white-space:nowrap}

/* help */
.help{left:0;top:1987px;width:1200px;height:513px;background:var(--blue)}
.help-title{left:75px;top:2046px;font-size:43px;font-weight:700;color:var(--white);letter-spacing:-0.5px}
.faq-row{left:60px;width:937px;height:51px;background:var(--green);color:var(--white);font-size:27.5px;letter-spacing:-0.2px;padding:0 16px;display:flex;align-items:center;justify-content:space-between;white-space:nowrap;overflow:hidden}
.faq-row .plus{font-size:34px;font-weight:400;margin-right:4px}
.show-more{left:60px;top:2424px;color:var(--white);font-size:23px;font-weight:600;text-decoration:underline}

/* support */
.live-card{left:75px;top:2548px;width:516px;height:233px;background:var(--blue)}
.live-photo{left:75px;top:2548px;width:248px;height:233px;background:linear-gradient(135deg,#4a4f58,#a88a78 55%,#d8d2cc)}
.live-card-body{left:342px;top:2560px;color:var(--white)}
.card-title{font-size:23px;font-weight:600;letter-spacing:-0.3px}
.card-title .g{color:var(--green)}
.live-card-body p{font-size:15px;line-height:22px;margin-top:14px}
.contact-line{display:flex;align-items:center;gap:16px;font-size:15px}
.agent-card{left:609px;top:2548px;width:515px;height:233px;background:var(--panel)}
.agent-art{left:628px;top:2572px;width:125px;height:190px;border-radius:40px 40px 30px 30px;background:linear-gradient(180deg,#2f6fd1,#1d4ea8)}
.agent-body{left:769px;top:2564px;width:340px}
.agent-body .card-title{color:var(--blue)}
.agent-body p{font-size:14.5px;line-height:28px;color:var(--ink);margin-top:12px}

/* footer */
.footer{left:0;top:2840px;width:1200px;height:229px;background:var(--panel)}
.footer-logo{left:74px;top:2887px;width:216px;height:72px;background:var(--white);display:flex;align-items:center;justify-content:center}
.footer-logo .brand{font-size:30px}
.footer-col{top:2866px;font-size:15px;color:var(--muted);line-height:24.5px;white-space:nowrap}
.footer-col h4{font-size:15px;font-weight:500;margin-bottom:18px}
.copyright{left:77px;top:3037px;font-size:11px;color:var(--muted);font-weight:500}
</style>
</head>
<body>

<!-- header -->
<div class="abs brand" style="left:77px;top:44px">CoverLantern</div>
<nav class="abs site-nav">
  <a class="active">Free Quote</a><a>No Exam</a><a>Articles</a><a>FAQ</a><a>About</a><a>Contact</a>
</nav>

<!-- hero -->
<h1 class="abs hero-title">Life insurance for a<br><span class="g">worryfree</span> life</h1>
<p class="abs hero-lede">Lorem ipsum dolor sit amet, consectetur adipiscing elit, sed do eiusmod tempor incididunt ut labore et</p>
<div class="abs quote-label">Get a quote for term life insurance</div>
<div class="abs state-select">State
  <svg width="16" height="9" viewBox="0 0 16 9"><path d="M0 0h16L8 9z" fill="#8b9096"/></svg>
</div>
<div class="abs btn quote-btn">Get My Quote</div>
<svg class="abs hero-art" viewBox="670 140 490 470" role="img" aria-label="Smiling family of three sitting together in casual clothes">
  <defs>
    <linearGradient id="family" x1="0" y1="0" x2="0" y2="1">
      <stop offset="0" stop-color="#e8d2c0"/><stop offset="0.5" stop-color="#c9c4bc"/><stop offset="1" stop-color="#3f6a9e"/>
    </linearGradient>
    <clipPath id="heroClip"><circle cx="888" cy="369" r="209"/><rect x="670" y="369" width="380" height="240"/></clipPath>
  </defs>
  <circle cx="1049" cy="489" r="101" fill="var(--dark)"/>
  <circle cx="739" cy="203" r="57" fill="var(--blue)"/>
  <circle cx="888" cy="369" r="209" fill="var(--green)"/>
  <path clip-path="url(#heroClip)" d="M700 360 Q720 200 850 180 Q990 185 1020 300 L1030 430 Q1040 560 950 590 L690 590 Q670 470 700 360Z" fill="url(#family)"/>
</svg>

<!-- how it works -->
<section class="abs how"></section>
<h2 class="abs section-title how-title">How It <span class="g">Works</span></h2>
<div class="abs step" style="left:79px"><span class="step-num">1</span><h3>Receive Your Quote</h3><p>Get an instant online Life Insurance quote for the benefit and term amount that best suits your needs.</p></div>
<div class="abs step" style="left:431px;top:845px"><span class="step-num">2</span><h3>Apply Online in Minutes</h3><p>After you choose your plan, you can complete your application online.&nbsp; It’s simple and only takes about 10 minutes.</p></div>
<div class="abs step" style="left:787px"><span class="step-num">3</span><h3>Complete Your Application</h3><p>Our underwriters will review your application.&nbsp; Once approved, your policy can be in-force within a few short days.&nbsp; It’s really that simple!</p></div>
<a class="abs step-link" style="left:122px">Get Quote</a>
<a class="abs step-link" style="left:475px">Apply Now</a>
<a class="abs step-link" style="left:831px">Get Started</a>

<!-- compare -->
<h2 class="abs section-title compare-title">Compare and <span class="g">Save</span></h2>
<ul class="abs bullets">
  <li>Get Quotes without having to enter your contact information.</li>
  <li>Decide what’s best for you without having to deal with pushy insurance agents.</li>
  <li>Virtual agent tools are available to help you choose what life insurance policy is best for you and your family.</li>
</ul>
<div class="abs btn compare-btn">Compare Carriers</div>

<svg class="abs" style="left:720px;top:1170px" width="405" height="195" viewBox="0 0 405 195">
  <g stroke="var(--green)" stroke-width="3" stroke-linecap="round">
    <path d="M18 8 L36 28"/><path d="M6 30 L32 40"/><path d="M5 135 L30 145"/><path d="M18 168 L34 152"/>
    <path d="M387 8 L369 28"/><path d="M399 30 L373 40"/><path d="M400 135 L375 145"/><path d="M387 168 L371 152"/>
  </g>
</svg>
<div class="abs rate-card best" style="top:1210px">
  <div class="carrier">Northvale</div>
  <div class="terms">$2,000,000 Death Benefit<br>20 Year Level Term
    <div class="price"><small>$</small>18<i>.08<br>/MO</i></div></div>
</div>
<div class="abs rate-card" style="top:1341px">
  <div class="carrier">Guardwell</div>
  <div class="terms">$2,000,000 Death Benefit<br>20 Year Level Term
    <div class="price"><small>$</small>21<i>.17<br>/MO</i></div></div>
</div>
<div class="abs rate-card" style="top:1472px">
  <div class="carrier" style="color:var(--blue);font-size:34px">KRT</div>
  <div class="terms">$2,000,000 Death Benefit<br>20 Year Level Term
    <div class="price"><small>$</small>23<i>.28<br>/MO</i></div></div>
</div>

<!-- trusted carriers -->
<section class="abs trusted"></section>
<h2 class="abs section-title trusted-title">We compare trusted life<br>insurance companies to find you<br>our <span class="g">best deals</span></h2>
<div class="abs carrier-tile" style="left:834px;top:1668px;width:140px;height:90px;font-size:20px">Northvale</div>
<div class="abs carrier-tile" style="left:984px;top:1668px;width:140px;height:90px;font-size:17px">Elmford Mutual</div>
<div class="abs carrier-tile" style="left:806px;top:1768px;width:168px;height:90px;font-size:23px">Pennant Life</div>
<div class="abs carrier-tile" style="left:984px;top:1768px;width:140px;height:90px;font-size:22px;font-weight:500">Guardwell</div>
<div class="abs carrier-tile" style="left:834px;top:1867px;width:140px;height:90px;font-size:34px;font-weight:500">KRT</div>
<div class="abs carrier-tile" style="left:984px;top:1867px;width:140px;height:90px;font-size:21px">Harborline</div>

<!-- help -->
<section class="abs help"></section>
<h2 class="abs help-title">Need More Help ?</h2>
<div class="abs faq-row" style="top:2126px"><span>How do I determine how much life insurance I need?</span><span class="plus">+</span></div>
<div class="abs faq-row" style="top:2197px"><span>Does buying a policy through CoverLantern save me money?</span><span class="plus">+</span></div>
<div class="abs faq-row" style="top:2268px"><span>How do I apply for Life Insurance on the CoverLantern website?</span><span class="plus">+</span></div>
<div class="abs faq-row" style="top:2338px"><span>Can I speak with a live agent?</span><span class="plus">+</span></div>
<a class="abs show-more">Show More</a>

<!-- support -->
<div class="abs live-card"></div>
<div class="abs live-photo" role="img" aria-label="Call centre agent with headset smiling at her desk, colleagues behind"></div>
<div class="abs live-card-body">
  <div class="card-title">Live Agent <span class="g">Support</span></div>
  <p>If you need a Live Agent,<br>CoverLantern has you covered.</p>
  <div class="contact-line" style="margin-top:34px">
    <svg width="18" height="18" viewBox="0 0 24 24"><path d="M6.6 10.8a15 15 0 0 0 6.6 6.6l2.2-2.2a1 1 0 0 1 1-.25 11.4 11.4 0 0 0 3.6.57 1 1 0 0 1 1 1V20a1 1 0 0 1-1 1A17 17 0 0 1 3 4a1 1 0 0 1 1-1h3.5a1 1 0 0 1 1 1c0 1.25.2 2.45.57 3.57a1 1 0 0 1-.25 1z" fill="#fff"/></svg>
    1-888-530-LAMP(5267)</div>
  <div class="contact-line" style="margin-top:16px">
    <svg width="18" height="14" viewBox="0 0 18 14"><rect width="18" height="14" rx="2" fill="#fff"/><path d="M1 2l8 6 8-6" stroke="var(--blue)" stroke-width="1.6" fill="none"/></svg>
    info@coverlantern.com</div>
</div>

<div class="abs agent-card"></div>
<div class="abs agent-art" role="img" aria-label="Blue robot mascot character holding a clipboard"></div>
<div class="abs agent-body">
  <div class="card-title">Virtual <span class="g">Agent</span></div>
  <p>Our Virtual Agent Lumi can help you<br>calculate how much death benefit you need.<br>Lumi can help you figure out what type of<br>Life Insurance is right for you and your family.</p>
</div>

<!-- footer -->
<footer class="abs footer"></footer>
<div class="abs footer-logo"><span class="brand">CoverLantern</span></div>
<div class="abs footer-col" style="left:449px"><h4>Company</h4>Free Quote<br>No Exam<br>Articles<br>About</div>
<div class="abs footer-col" style="left:595px"><h4>Support</h4>FAQ<br>How It Works</div>
<div class="abs footer-col" style="left:756px"><h4>Connect</h4>Returns<br>Warranty<br>Contact<br>Blog<br>Get $15</div>
<div class="abs footer-col" style="left:887px"><h4>Follow Us</h4>FaceSpace<br>Snapgrid<br>Chirper</div>
<div class="abs footer-col" style="left:1025px;top:2869px"><h4>Our Policies</h4>Privacy Policy<br>Terms of Use</div>
<div class="abs copyright">© 2022 CoverLantern. All Rights Reserved</div>

</body>
</html>
```